Business Cards & Stationary for Broadcast Company

We are a satellite company launching a new exciting brand by the name of "Veloran". Veloran is a broadcasting solution provider that gives end-to-end solutions to TV channels and other content providers to deliver and distribute their content globally. Weather it be TV channels that need to be broadcasted in their local regions or internationally, or its collection of news from various locations, or even coverage of special sports or other events, we provide the technology and services to make that happen.
we need a design for business cards as our top priority but also require letterhead and envelope design as well.
Business card will include the following information
Name: Karim Yusof
Designation: General Manager
Mobile (M): +92 321 4718296
+971 50 2846193 (UAE)
Direct (D): +92 213 4609142
Office (O): +92 213 4602518-22
Fax (F): +92 213 4609142
Email (E): karim@veloran.biz
Website: www.veloran.biz

```html
<!DOCTYPE html>
<html lang="en">
<head>
<meta charset="utf-8">
<title>Veloran Business Card</title>
<link href="https://fonts.googleapis.com/css2?family=Roboto:wght@400;700&display=swap" rel="stylesheet">
<style>
  :root {
    --bg: #e4e5e8;
    --navy: #0d4a80;
    --blue: #1565b0;
    --green: #a6ce39;
    --red: #e3262d;
    --ink: #4a4a4a;
    --paper: #f7f7f7;
    --white: #ffffff;
  }
  * { box-sizing: border-box; margin: 0; padding: 0; }
  html, body { width: 1200px; height: 800px; overflow: hidden; }
  body {
    background: var(--bg);
    font-family: "Roboto", Arial, sans-serif;
    position: relative;
  }
  .card {
    position: absolute;
    top: 250px;
    width: 520px;
    height: 300px;
    box-shadow: 0 6px 18px rgba(0,0,0,0.12);
    overflow: hidden;
  }
  .card-front { left: 60px; background: var(--navy); }
  .card-back { left: 620px; background: var(--paper); }

  .brand {
    position: absolute;
    display: flex;
    align-items: center;
    gap: 10px;
  }
  .brand-dot {
    width: 14px; height: 14px; border-radius: 50%;
    background: var(--green);
  }
  .brand-name {
    font-weight: 700;
    font-size: 30px;
    letter-spacing: 1px;
  }
  .card-front .brand { left: 50px; top: 128px; }
  .card-front .brand-name { color: var(--white); }
  .card-back .brand { left: 150px; top: 44px; }
  .card-back .brand-name { color: var(--blue); }

  .divider {
    position: absolute;
    left: 270px; top: 100px;
    width: 1px; height: 100px;
    background: rgba(255,255,255,0.8);
  }
  .front-web {
    position: absolute;
    left: 300px; top: 141px;
    color: var(--white);
    font-size: 14px;
  }

  .person { position: absolute; left: 44px; top: 120px; }
  .person-name { color: var(--blue); font-weight: 700; font-size: 18px; }
  .person-title { color: var(--ink); font-size: 12px; margin-top: 2px; }

  .contacts {
    position: absolute;
    right: 28px; top: 104px;
    list-style: none;
    text-align: right;
  }
  .contact {
    display: flex;
    justify-content: flex-end;
    align-items: center;
    gap: 8px;
    color: var(--ink);
    font-size: 12.5px;
    line-height: 18px;
  }
  .contact svg { width: 11px; height: 11px; flex: none; }
  .contact .spacer { width: 11px; flex: none; }

  .footer-band { position: absolute; left: 0; bottom: 0; }
</style>
</head>
<body>

<section class="card card-front">
  <div class="brand">
    <span class="brand-dot"></span>
    <span class="brand-name">VELORAN</span>
  </div>
  <div class="divider"></div>
  <p class="front-web">www.veloran.biz</p>
</section>

<section class="card card-back">
  <div class="brand">
    <span class="brand-dot"></span>
    <span class="brand-name">VELORAN</span>
  </div>

  <div class="person">
    <p class="person-name">Karim Yusof</p>
    <p class="person-title">General Manager</p>
  </div>

  <ul class="contacts">
    <li class="contact">+92 321 4718296
      <svg viewBox="0 0 12 12"><rect width="12" height="12" rx="2" fill="var(--red)"/><rect x="4" y="2" width="4" height="8" rx="1" fill="#fff"/></svg></li>
    <li class="contact">+971 50 2846193 (UAE)
      <svg viewBox="0 0 12 12"><rect width="12" height="12" rx="2" fill="var(--red)"/><rect x="4" y="2" width="4" height="8" rx="1" fill="#fff"/></svg></li>
    <li class="contact">karim@veloran.biz
      <svg viewBox="0 0 12 12"><rect width="12" height="12" rx="2" fill="var(--red)"/><rect x="2.5" y="3.5" width="7" height="5" fill="#fff"/><path d="M2.5 3.5 6 6.5 9.5 3.5" stroke="var(--red)" stroke-width="1" fill="none"/></svg></li>
    <li class="contact">+92 213 4609142 (Direct)
      <svg viewBox="0 0 12 12"><rect width="12" height="12" rx="2" fill="var(--red)"/><path d="M3 3h2l1 2-1 1a5 5 0 0 0 2 2l1-1 2 1v2A7 7 0 0 1 3 3z" fill="#fff"/></svg></li>
    <li class="contact">+92 213 4602518-22 (Office)
      <svg viewBox="0 0 12 12"><rect width="12" height="12" rx="2" fill="var(--red)"/><path d="M3 3h2l1 2-1 1a5 5 0 0 0 2 2l1-1 2 1v2A7 7 0 0 1 3 3z" fill="#fff"/></svg></li>
    <li class="contact">+92 213 4609142
      <svg viewBox="0 0 12 12"><rect width="12" height="12" rx="2" fill="var(--red)"/><rect x="3" y="5" width="6" height="4" fill="#fff"/><rect x="4" y="2.5" width="4" height="2" fill="#fff"/></svg></li>
    <li class="contact">www.veloran.biz
      <svg viewBox="0 0 12 12"><rect width="12" height="12" rx="2" fill="var(--red)"/><circle cx="6" cy="6" r="3.5" stroke="#fff" fill="none"/><path d="M2.5 6h7M6 2.5v7" stroke="#fff" stroke-width="0.8"/></svg></li>
  </ul>

  <svg class="footer-band" width="520" height="60" viewBox="0 0 520 60">
    <polygon points="0,32 300,32 272,60 0,60" fill="var(--navy)"/>
    <polygon points="300,0 520,0 520,60 238,60" fill="var(--green)"/>
    <polygon points="300,0 306,0 272,32 266,32" fill="var(--navy)"/>
  </svg>
</section>

</body>
</html>
```